Business Cards for our company

Hi there,

we have successfully designed a logo with ArtFlock and would like now to design our business cards. We would like to keep the colours and the look-and-feel of the logo. Please send in variations with two or three colours and one or two sides. I promise to respond to every single submission.

Many thanks and happy new year.

All the best,
Wilfried

Target Market(s)

B2B

Industry/Entity Type

Trade

Contact Information for Business Card

We have successfully designed a logo with ArtFlock and would like now to design our business cards. We would like to keep the colours and the look-and-feel of the logo. Please send in variations with two or three colours and one or two sides. I promise to respond to every single submission.

Font styles to use
Serif
Sans Serif
Script

Requirements
Must have
• These information should be on the business card, grouped as you suggest, and we think using small pictograms for mobile, email, etc is pretty helpful:
• Wilfried Tammler (first and second name)
• Geschäftsführer/ Managing Director (title)
• KoR Warenkontor GmbH (company name and legal form)
• Ostheimer Str. 18/3 (street and house number)
• 70839 Gerlingen (zip code and town)
• +491709384562 (mobile)
• +4971569027341 (work)
• w.tammler@kor-warenkontor.example (email)
• www.kor-warenkontor.example (web)
Nice to have
• Spectacular and interesting layout and design. You look at it and think, wow, that's not the normal stuff.
• We think of ourselves as bridge-builders between businesses (international producers on the one hand, and retail chains on the other hand) and we translate, organise and manage projects where both partners are involved, but it's difficult for them to cooperate due to language barriers and different working cultures.
• This is why we have the n between the B's shaped as a bridge, and the green arc supports this idea. Maybe you could play with this idea...
Should not have
• the standard layout that everybody has

```html
<!DOCTYPE html>
<html lang="en">
<head>
<meta charset="utf-8">
<title>KoR Warenkontor – Business Card</title>
<link rel="stylesheet" href="https://fonts.googleapis.com/css2?family=Arimo:wght@400;700&display=swap">
<style>
  :root {
    --backdrop: #9b9b9b;
    --paper: #f7f7f5;
    --ink: #111111;
    --brand-green: #3cc35f;
    --brand-green-light: #5fd07d;
    --band-black: #0b0b0b;
  }
  html, body {
    margin: 0;
    padding: 0;
    width: 1200px;
    height: 1200px;
    overflow: hidden;
    background: var(--backdrop);
    font-family: "Arimo", Arial, sans-serif;
  }
  .stage {
    position: relative;
    width: 1200px;
    height: 1200px;
  }
  .card {
    position: absolute;
    left: 100px;
    top: 314px;
    width: 1000px;
    height: 572px;
    background: var(--paper);
    overflow: hidden;
    box-shadow: 0 20px 40px rgba(0,0,0,0.25);
  }
  .card__shapes {
    position: absolute;
    inset: 0;
  }
  .brand {
    position: absolute;
    left: 60px;
    top: 228px;
    display: flex;
    align-items: flex-start;
    gap: 14px;
  }
  .brand__dot {
    width: 18px;
    height: 18px;
    margin-top: 10px;
    border-radius: 50%;
    background: var(--brand-green);
    flex: none;
  }
  .brand__name {
    margin: 0;
    font-weight: 700;
    font-size: 30px;
    line-height: 1.15;
    color: var(--ink);
  }
  .brand__line {
    display: block;
  }
  .person {
    position: absolute;
    left: 60px;
    top: 350px;
    color: var(--ink);
  }
  .person__name {
    margin: 0;
    font-weight: 700;
    font-size: 26px;
  }
  .person__title {
    margin: 6px 0 0;
    font-weight: 400;
    font-size: 18px;
  }
  .contact {
    position: absolute;
    right: 50px;
    top: 160px;
    margin: 0;
    padding: 0;
    list-style: none;
    color: var(--ink);
    font-size: 17px;
  }
  .contact__item {
    display: flex;
    justify-content: flex-end;
    align-items: center;
    gap: 12px;
    height: 42px;
    white-space: nowrap;
  }
  .contact__icon {
    width: 22px;
    height: 22px;
    flex: none;
  }
</style>
</head>
<body>
<main class="stage">
  <article class="card" aria-label="KoR Warenkontor business card">
    <svg class="card__shapes" viewBox="0 0 1000 572" width="1000" height="572" aria-hidden="true">
      <defs>
        <linearGradient id="green-panel" x1="0" y1="0" x2="1" y2="1">
          <stop offset="0" stop-color="#5fd07d"/>
          <stop offset="1" stop-color="#3cc35f"/>
        </linearGradient>
      </defs>
      <path class="band-black" fill="#0b0b0b"
            d="M300,0 C430,120 500,330 515,572 L590,572 C575,330 520,140 420,0 Z"/>
      <path class="panel-green" fill="url(#green-panel)"
            d="M440,0 C545,140 588,330 600,572 L1000,572 L1000,0 Z"/>
    </svg>

    <div class="brand">
      <span class="brand__dot"></span>
      <h1 class="brand__name">
        <span class="brand__line">KoR Warenkontor</span>
        <span class="brand__line">GmbH</span>
      </h1>
    </div>

    <div class="person">
      <p class="person__name">Wilfried Tammler</p>
      <p class="person__title">Managing Director</p>
    </div>

    <ul class="contact">
      <li class="contact__item">+491709384562
        <svg class="contact__icon" viewBox="0 0 24 24"><rect width="24" height="24" fill="#111111"/><rect x="8" y="4" width="8" height="16" rx="1.5" fill="none" stroke="#3cc35f" stroke-width="1.8"/><circle cx="12" cy="17" r="1" fill="#3cc35f"/></svg>
      </li>
      <li class="contact__item">+4971569027341
        <svg class="contact__icon" viewBox="0 0 24 24"><rect width="24" height="24" fill="#111111"/><path d="M7 5 L10 5 L11 9 L9 10.5 C10 13 11 14 13.5 15 L15 13 L19 14 L19 17 C19 18 18 19 17 19 C10 19 5 14 5 7 C5 6 6 5 7 5 Z" fill="#3cc35f"/></svg>
      </li>
      <li class="contact__item">Ostheimer Str. 18/3, 70839 Gerlingen
        <svg class="contact__icon" viewBox="0 0 24 24"><rect width="24" height="24" fill="#111111"/><path d="M12 4 C8.7 4 7 6.4 7 9 C7 12.5 12 19 12 19 C12 19 17 12.5 17 9 C17 6.4 15.3 4 12 4 Z" fill="#3cc35f"/><circle cx="12" cy="9" r="2" fill="#111111"/></svg>
      </li>
      <li class="contact__item">www.kor-warenkontor.example
        <svg class="contact__icon" viewBox="0 0 24 24"><rect width="24" height="24" fill="#111111"/><g fill="none" stroke="#3cc35f" stroke-width="1.5"><circle cx="12" cy="12" r="7"/><ellipse cx="12" cy="12" rx="3" ry="7"/><line x1="5" y1="12" x2="19" y2="12"/></g></svg>
      </li>
      <li class="contact__item">w.tammler@kor-warenkontor.example
        <svg class="contact__icon" viewBox="0 0 24 24"><rect width="24" height="24" fill="#111111"/><rect x="5" y="7" width="14" height="10" fill="none" stroke="#3cc35f" stroke-width="1.6"/><path d="M5 7 L12 13 L19 7" fill="none" stroke="#3cc35f" stroke-width="1.6"/></svg>
      </li>
    </ul>
  </article>
</main>
</body>
</html>
```